Business Card Design

We need a design for business cards for our company. We have a logo. We teach EMT's and we are based out of Virginia. The information that will need to add would be, name, title, phone number, email, address. On the back of the business card would be "We help you, help others"

Target Market(s)

People that want to become EMT's

Colors

Designer to choose colors to be used in the design.

Requirements
Must have
• company logo

```html
<!DOCTYPE html>
<html lang="en">
<head>
<meta charset="utf-8">
<title>CareStep Training — Business Card</title>
<link rel="stylesheet" href="https://fonts.googleapis.com/css2?family=Montserrat:wght@400;500;600;700&family=Roboto:wght@400;500&display=swap">
<style>
  :root {
    --navy: #243240;
    --navy-deep: #1d2935;
    --red: #c9233b;
    --paper: #f2f2f2;
    --paper-shade: #e3e3e3;
    --ink-light: #e9edf1;
    --ink-muted: #c5ccd3;
    --backdrop: #d8d3cb;
  }
  * { box-sizing: border-box; margin: 0; padding: 0; }
  html, body {
    width: 1200px; height: 780px; overflow: hidden;
    background: var(--backdrop);
  }
  .canvas {
    position: relative; width: 1200px; height: 780px;
  }
  .card {
    position: absolute; top: 235px;
    width: 540px; height: 310px;
    border-radius: 16px; overflow: hidden;
    box-shadow: 0 10px 28px rgba(0,0,0,.25);
  }
  /* Front */
  .card-front { left: 45px; background: var(--navy); }
  .front-brand {
    height: 130px;
    background: linear-gradient(180deg, #fafafa, var(--paper-shade));
    display: flex; align-items: center; padding-left: 44px; gap: 14px;
  }
  .brand-dot {
    width: 30px; height: 30px; border-radius: 50%;
    background: var(--red);
  }
  .brand-name {
    font-family: 'Montserrat', sans-serif; font-weight: 600;
    font-size: 34px; letter-spacing: -0.5px; color: var(--red);
  }
  .front-band {
    height: 44px; background: var(--red);
    display: flex; align-items: center; padding-left: 44px;
    font-family: 'Roboto', sans-serif; color: #fff;
  }
  .person-name { font-size: 19px; font-weight: 500; letter-spacing: .3px; }
  .divider { margin: 0 10px; font-size: 19px; }
  .person-title { font-size: 14px; }
  .front-details {
    position: relative; height: 136px;
    background: linear-gradient(180deg, var(--navy), var(--navy-deep));
    font-family: 'Roboto', sans-serif; color: var(--ink-light);
  }
  .contact-list {
    position: absolute; left: 44px; bottom: 20px;
    list-style: none; font-size: 13.5px; line-height: 22px;
  }
  .contact-list li { display: flex; align-items: center; gap: 12px; }
  .contact-list svg { width: 13px; height: 13px; flex: none; }
  .address {
    position: absolute; right: 34px; top: 22px;
    font-size: 13.5px; line-height: 21px; text-align: left;
  }
  /* Back */
  .card-back {
    left: 615px;
    background: radial-gradient(ellipse at 45% 45%, #2a3a49, var(--navy-deep));
    display: flex; align-items: center; justify-content: center;
  }
  .tagline {
    font-family: 'Montserrat', sans-serif; font-weight: 500;
    font-size: 22px; letter-spacing: 5px; color: var(--ink-muted);
    text-shadow: 0 1px 2px rgba(0,0,0,.5);
  }
  .tagline .accent { color: var(--red); }
</style>
</head>
<body>
<main class="canvas">
  <section class="card card-front">
    <div class="front-brand">
      <span class="brand-dot"></span>
      <span class="brand-name">CARESTEP TRAINING</span>
    </div>
    <div class="front-band">
      <span class="person-name">JORDAN R. HALE</span>
      <span class="divider">|</span>
      <span class="person-title">Managing Director</span>
    </div>
    <div class="front-details">
      <ul class="contact-list">
        <li>
          <svg viewBox="0 0 14 14"><rect x="1.5" y="1.5" width="11" height="11" rx="1.5" fill="none" stroke="#e9edf1" stroke-width="1.5"/></svg>
          +1 540 555 0148
        </li>
        <li>
          <svg viewBox="0 0 14 14"><rect x="0.5" y="2.5" width="13" height="9" fill="#e9edf1"/><path d="M0.5 2.5 L7 8 L13.5 2.5" fill="none" stroke="#243240" stroke-width="1.2"/></svg>
          hello@carestep.example
        </li>
        <li>
          <svg viewBox="0 0 14 14"><circle cx="7" cy="7" r="6.5" fill="#e9edf1"/><path d="M0.5 7 H13.5 M7 0.5 V13.5 M3 2.5 Q7 5 11 2.5 M3 11.5 Q7 9 11 11.5" fill="none" stroke="#243240" stroke-width="0.9"/></svg>
          www.carestep.example
        </li>
      </ul>
      <p class="address">PO Box 48, Harbor Lane<br>Richmond, Virginia</p>
    </div>
  </section>

  <section class="card card-back">
    <p class="tagline">WE <span class="accent">HELP</span> YOU, <span class="accent">HELP</span> OTHERS</p>
  </section>
</main>
</body>
</html>
```